Ad design for a macarons brand

We are a dessert brand with one product line: macarons. Our products delight. Every bite is a dream!

We are launching a new product and would like to lunch a small tactical campaign for the product to boost sales.

The new macron is mango ganache and the middle a mix of sour mango and yuzu (https://www.plumvetra.com/what-is-yuzu-481630).

Here are some images we took of the new macaron
https://www.farnlooq.com/sh/tqzp8mwrhkd2aly/QWXeLpTn-vyRsdfKuJmNoP3Zt?dl=0

I attach the brand guideline document.

Required sizes

1080 x 1350
1080 x 1920

```html
<!DOCTYPE html>
<html lang="en">
<head>
<meta charset="utf-8">
<title>Macarons Campaign Layouts</title>
<link rel="stylesheet" href="https://fonts.googleapis.com/css2?family=Playfair+Display:wght@400;900&family=Outfit:wght@300;400&display=swap">
<style>
  :root {
    --stage: #d4d4d4;
    --paper: #ffffff;
    --ink: #111111;
    --mango: #f2a90f;
    --photo-light: #f7d25a;
    --photo-mid: #f0a23a;
    --photo-deep: #d98a2a;
    --photo-leaf: #a8c25a;
  }
  * { margin: 0; padding: 0; box-sizing: border-box; }
  html, body { width: 1200px; height: 1200px; overflow: hidden; }
  body { background: var(--stage); position: relative; }

  .ad { position: absolute; top: 200px; height: 800px; background: var(--paper); overflow: hidden; }
  .ad--feed { left: 40px; width: 640px; }
  .ad--story { left: 710px; width: 450px; }

  .ad__art { position: absolute; inset: 0; width: 100%; height: 100%; }

  .ad__text { position: absolute; line-height: 1; white-space: nowrap; }
  .title { font-family: "Playfair Display", serif; font-weight: 400; color: var(--ink); letter-spacing: -0.02em; }
  .subtitle { font-family: "Outfit", sans-serif; font-weight: 300; color: var(--mango); }
  .headline { font-family: "Playfair Display", serif; font-weight: 400; color: var(--ink); letter-spacing: -0.03em; line-height: 0.95; }
  .headline__accent { font-weight: 900; color: var(--mango); display: block; }
  .flavour { font-family: "Outfit", sans-serif; font-weight: 400; color: var(--ink); letter-spacing: 0.08em; line-height: 1.35; }
  .flavour__tag { color: var(--mango); }
  .brand { font-family: "Playfair Display", serif; font-weight: 400; color: var(--ink); }

  .ad--feed .title { left: 44px; top: 58px; font-size: 64px; }
  .ad--feed .subtitle { left: 46px; top: 132px; font-size: 24px; }
  .ad--feed .headline { left: 46px; top: 206px; font-size: 62px; }
  .ad--feed .flavour { left: 48px; top: 416px; font-size: 17px; }
  .ad--feed .brand { left: 44px; top: 700px; font-size: 50px; }

  .ad--story .title { left: 32px; top: 44px; font-size: 50px; }
  .ad--story .subtitle { left: 33px; top: 102px; font-size: 19px; }
  .ad--story .headline { left: 33px; top: 150px; font-size: 46px; }
  .ad--story .flavour { left: 34px; top: 300px; font-size: 13px; }
  .ad--story .brand { left: 32px; top: 716px; font-size: 42px; }
</style>
</head>
<body>

<section class="ad ad--feed">
  <svg class="ad__art" viewBox="0 0 640 800">
    <defs>
      <linearGradient id="feedPhotoTone" x1="0.3" y1="0" x2="0.6" y2="1">
        <stop offset="0" stop-color="var(--photo-light)"/>
        <stop offset="0.22" stop-color="var(--photo-leaf)"/>
        <stop offset="0.5" stop-color="var(--photo-mid)"/>
        <stop offset="1" stop-color="var(--photo-deep)"/>
      </linearGradient>
    </defs>
    <path role="img" aria-label="Photo of stacked mango yuzu macarons with mango slices behind"
      d="M500 0 C480 130 490 260 430 360 C370 450 290 480 300 600 C310 700 380 735 450 715 C530 692 570 650 640 660 L640 0 Z"
      fill="url(#feedPhotoTone)"/>
    <path d="M486 0 C464 130 472 255 414 352 C354 444 272 476 284 604 C296 716 376 752 452 730 C532 707 572 668 640 676"
      fill="none" stroke="var(--mango)" stroke-width="1.5"/>
  </svg>
  <h1 class="ad__text title">MACARONS</h1>
  <p class="ad__text subtitle">OUR PRODUCTS DELIGHT</p>
  <p class="ad__text headline">EVERY<br>BITE IS A<span class="headline__accent">DREAM!</span></p>
  <p class="ad__text flavour"><span class="flavour__tag">NEW</span> · MANGO GANACHE<br>SOUR MANGO &amp; YUZU</p>
  <p class="ad__text brand">Velune</p>
</section>

<section class="ad ad--story">
  <svg class="ad__art" viewBox="0 0 450 800">
    <defs>
      <linearGradient id="storyPhotoTone" x1="0.3" y1="0" x2="0.6" y2="1">
        <stop offset="0" stop-color="var(--photo-light)"/>
        <stop offset="0.22" stop-color="var(--photo-leaf)"/>
        <stop offset="0.5" stop-color="var(--photo-mid)"/>
        <stop offset="1" stop-color="var(--photo-deep)"/>
      </linearGradient>
    </defs>
    <path role="img" aria-label="Photo of stacked mango yuzu macarons with mango slices behind"
      d="M450 110 C425 220 410 310 320 360 C220 412 70 400 52 490 C34 580 90 650 180 660 C280 670 340 620 450 636 Z"
      fill="url(#storyPhotoTone)"/>
    <path d="M450 92 C420 210 400 298 310 346 C210 398 56 388 38 488 C20 590 84 668 182 676 C284 684 344 638 450 652"
      fill="none" stroke="var(--mango)" stroke-width="1.5"/>
  </svg>
  <h1 class="ad__text title">MACARONS</h1>
  <p class="ad__text subtitle">OUR PRODUCTS DELIGHT</p>
  <p class="ad__text headline">EVERY<br>BITE IS A<span class="headline__accent">DREAM!</span></p>
  <p class="ad__text flavour"><span class="flavour__tag">NEW</span> · MANGO GANACHE<br>SOUR MANGO &amp; YUZU</p>
  <p class="ad__text brand">Velune</p>
</section>

</body>
</html>
```